Stylish Business Card for Modern hair salon

I need a simple business card design using our salon logo and colours that are in the logo. We service clients of all ages but predominantly those in the 18 to 55 age range. We have a young staff and are looking to have a card that will present a modern and clean image that represents who we are. The card should be in black and white same as our logo. Minimal use of other colours is allowed.

Industry/Entity Type

Hair And Beauty

Contact Information for Business Card

The design should have the following information
salon name - TR Hair Studio
address - 2751 Birchfield Rd.E. Mississauga, ON L7P3K2
phone - 905 614-2870
website - trhairexample.ca
instagram - tr.hairstudio
twitter - @TR_HairStudio

Colors
000000
ffffff
474747

Requirements
Must have
• simple design, salon name, address, phone, website, instagram, twitter info
• Back of card should have the following:
• YOUR NEXT APPOINTMENT
• DATE
• TIME
Nice to have
• simple design, clear to see and read,
• predominantly black and white colour, minimal use of other colours is ok
Should not have
• many colours, various fonts

```html
<!DOCTYPE html>
<html lang="en">
<head>
<meta charset="utf-8">
<title>TR Hair Studio – Business Card</title>
<link rel="stylesheet" href="https://fonts.googleapis.com/css2?family=Roboto:wght@400;500&family=Roboto+Condensed:wght@500&display=swap">
<style>
  :root {
    --ink: #000000;
    --paper: #ffffff;
    --grey: #474747;
    --name-grey: #d6d6d6;
    --backdrop: #e9e9e9;
    --card-white: #f4f4f4;
  }
  * { box-sizing: border-box; margin: 0; padding: 0; }
  html, body {
    width: 1200px; height: 960px; overflow: hidden;
    background: var(--backdrop);
    font-family: "Roboto", Arial, sans-serif;
  }
  .canvas { position: relative; width: 1200px; height: 960px; }
  .card {
    position: absolute; width: 600px; height: 342px;
    box-shadow: 0 4px 10px rgba(0,0,0,0.25);
  }
  .card-frame {
    position: absolute; top: 14px; left: 14px; right: 14px; bottom: 14px;
    border: 2px solid var(--paper);
  }
  .card--front { left: 315px; top: 113px; background: var(--ink); color: var(--paper); }
  .card--back { left: 312px; top: 472px; background: var(--card-white); color: var(--ink); }
  .card--back .card-frame { border-color: var(--ink); }

  .brand-name {
    position: absolute; font-family: "Roboto", Arial, sans-serif;
    font-weight: 500; letter-spacing: 1px; white-space: nowrap; text-align: center;
  }
  .card--front .brand-name { left: 60px; width: 250px; top: 152px; font-size: 28px; color: var(--paper); }
  .card--back .brand-name { left: 341px; width: 230px; top: 82px; font-size: 26px; color: var(--ink); }

  .divider {
    position: absolute; left: 320px; top: 72px; width: 2px; height: 222px;
    background: linear-gradient(to bottom, transparent, var(--grey) 20%, var(--grey) 80%, transparent);
  }
  .contact { position: absolute; left: 350px; top: 80px; }
  .contact__name {
    font-family: "Roboto Condensed", Arial, sans-serif; font-weight: 500;
    font-size: 21px; color: var(--name-grey); letter-spacing: 0.3px;
  }
  .contact__title { font-size: 14px; font-weight: 500; margin-top: 4px; letter-spacing: 0.3px; }
  .contact__address { font-size: 14px; line-height: 19px; margin-top: 10px; }
  .contact__list { list-style: none; margin-top: 10px; font-size: 14px; }
  .contact__list li { display: flex; align-items: center; height: 19px; }
  .contact__icon { width: 12px; height: 12px; margin-right: 12px; margin-left: 4px; flex: none; }

  .appointment { position: absolute; left: 56px; top: 192px; width: 486px; }
  .appointment__title { font-size: 19px; font-weight: 500; }
  .field-row { display: flex; align-items: baseline; font-size: 16px; margin-top: 23px; }
  .field-row + .field-row { margin-top: 21px; }
  .field-label { margin-right: 3px; }
  .field-line { flex: 1; border-bottom: 1px dotted var(--ink); height: 1px; margin-right: 4px; }
  .field-line--date { flex: 1.9; }
  .field-unit { font-size: 12px; margin-left: 2px; }
</style>
</head>
<body>
<main class="canvas">

  <section class="card card--front" aria-label="Front of business card">
    <div class="card-frame" aria-hidden="true"></div>

    <div class="brand-name">TR Hair Studio</div>
    <div class="divider"></div>

    <div class="contact">
      <p class="contact__name">ALEX MORENO</p>
      <p class="contact__title">CEO/FOUNDER</p>
      <p class="contact__address">2751 Birchfield Rd.E.<br>Mississauga, ON L7P3K2</p>
      <ul class="contact__list">
        <li>
          <svg class="contact__icon" viewBox="0 0 12 12" aria-hidden="true"><path d="M2.5 1 L4.5 3.2 L3.5 4.6 Q4.8 7.2 7.4 8.5 L8.8 7.5 L11 9.5 L9.6 11 Q5 10.5 1 2.4 Z" fill="#ffffff"/></svg>
          905 614-2870
        </li>
        <li>
          <svg class="contact__icon" viewBox="0 0 12 12" aria-hidden="true"><circle cx="6" cy="6" r="5" fill="none" stroke="#ffffff" stroke-width="1.4"/><line x1="1" y1="6" x2="11" y2="6" stroke="#ffffff" stroke-width="1"/><ellipse cx="6" cy="6" rx="2.2" ry="5" fill="none" stroke="#ffffff" stroke-width="1"/></svg>
          www.trhairexample.ca
        </li>
        <li>
          <svg class="contact__icon" viewBox="0 0 12 12" aria-hidden="true"><circle cx="6" cy="6" r="5" fill="#ffffff"/></svg>
          @TR_HairStudio
        </li>
        <li>
          <svg class="contact__icon" viewBox="0 0 12 12" aria-hidden="true"><rect x="1" y="1" width="10" height="10" fill="#ffffff"/></svg>
          tr.hairstudio
        </li>
      </ul>
    </div>
  </section>

  <section class="card card--back" aria-label="Back of business card">
    <div class="card-frame" aria-hidden="true"></div>

    <div class="brand-name">TR Hair Studio</div>

    <div class="appointment">
      <h2 class="appointment__title">Your Next Appointment</h2>
      <div class="field-row">
        <span class="field-label">Name:</span><span class="field-line"></span>
      </div>
      <div class="field-row">
        <span class="field-label">Date:</span><span class="field-line field-line--date"></span>
        <span class="field-label">Time:</span><span class="field-line"></span>
        <span class="field-unit">AM/PM</span>
      </div>
    </div>
  </section>

</main>
</body>
</html>
```